Business Card Design Project

Marla's Elixirs is a natural skincare business and we need a business card designed. The company focuses on natural products and will be launching with body scrubs and bath fizzies and our mission statement is: To deliver high quality natural beauty products at a good value. It's two cards - one design - the only information changing would be name and email address

Target Market(s)

Females ages 20-50

Industry/Entity Type

Business

Requirements
Must have
• Marla's Elixirs

Yvonne Hart-Becker
T: 800-555-7341
E: Yvonne@MarlasElixirs-example.com
W: www.MarlasElixirs-example.com

Tobias Werner
T: 800-555-7341
E: Tobias@MarlasElixirs-example.com
W: www.MarlasElixirs-example.com
Nice to have
• I'd like to use the colors or text found at www.marlaselixirs-example.com but I'm open to suggestions since design isn't set in stone yet. I would also like to have the words .....a little bit of magic somewhere under the company name in a different type of font. I would like a design that feels clean and maybe a retro feel to it - front and back would be nice but not mandatory

```html
<!DOCTYPE html>
<html lang="en">
<head>
<meta charset="utf-8">
<title>Marla's Elixirs – Business Card</title>
<link rel="stylesheet" href="https://fonts.googleapis.com/css2?family=Delius+Swash+Caps&family=Open+Sans:wght@400&display=swap">
<style>
  :root {
    --backdrop: #e8e5e2;
    --card: #fbfaf7;
    --plum: #6d1452;
    --ink: #2b2430;
    --ornament: #dcbfe0;
    --ornament-soft: #efe1f1;
    --band-text: #f3dcee;
  }
  * { margin: 0; padding: 0; box-sizing: border-box; }
  html, body {
    width: 1200px;
    height: 800px;
    overflow: hidden;
    background: var(--backdrop);
  }
  .canvas {
    position: relative;
    width: 1200px;
    height: 800px;
  }
  .business-card {
    position: absolute;
    left: 180px;
    top: 160px;
    width: 840px;
    height: 480px;
    background: var(--card);
    box-shadow: 0 10px 30px rgba(60, 40, 50, 0.18);
    overflow: hidden;
  }
  .ornament {
    position: absolute;
    border-radius: 48% 52% 40% 60% / 55% 45% 55% 45%;
    background: radial-gradient(ellipse at center, var(--ornament) 0%, var(--ornament-soft) 70%, transparent 100%);
    opacity: 0.85;
  }
  .ornament--top-right {
    right: 28px;
    top: 22px;
    width: 100px;
    height: 150px;
  }
  .ornament--bottom-left {
    left: 100px;
    top: 222px;
    width: 96px;
    height: 130px;
  }
  .brand {
    position: absolute;
    left: 0;
    right: 0;
    top: 84px;
    text-align: center;
    font-family: 'Open Sans', sans-serif;
    font-weight: 400;
    font-size: 48px;
    line-height: 1;
    color: var(--plum);
  }
  .person {
    position: absolute;
    left: 0;
    right: 0;
    top: 186px;
    text-align: center;
    font-family: 'Delius Swash Caps', cursive;
    font-weight: 400;
    font-size: 42px;
    color: var(--ink);
  }
  .contact {
    position: absolute;
    left: 0;
    right: 0;
    top: 280px;
    text-align: center;
    font-family: 'Open Sans', sans-serif;
    font-style: normal;
    font-size: 20px;
    line-height: 30px;
    color: var(--ink);
  }
  .web-band {
    position: absolute;
    left: 0;
    right: 0;
    top: 352px;
    height: 80px;
    background: var(--plum);
    display: flex;
    align-items: center;
    justify-content: center;
    font-family: 'Open Sans', sans-serif;
    font-size: 20px;
    letter-spacing: 4px;
    color: var(--band-text);
  }
</style>
</head>
<body>
  <main class="canvas">
    <article class="business-card">
      <div class="ornament ornament--top-right" role="img" aria-label="Lavender flourish with swirling leaves"></div>
      <div class="ornament ornament--bottom-left" role="img" aria-label="Lavender flourish with swirling leaves"></div>

      <header class="brand">Marla's Elixirs</header>

      <h1 class="person">Yvonne Hart-Becker</h1>

      <address class="contact">
        <div class="contact__phone">800-555-7341</div>
        <div class="contact__email">Yvonne@MarlasElixirs-example.com</div>
      </address>

      <footer class="web-band">www.MarlasElixirs-example.com</footer>
    </article>
  </main>
</body>
</html>
```